Brixley Travel letterhead design

We need a design for a simple document where we can dump our own information within it. A simple letterhead style. No address or phone details etc are required. More just our logo and free format. Hope this makes sense !

```html
<!DOCTYPE html>
<html lang="en">
<head>
<meta charset="utf-8">
<title>Brixley Travel Letterhead</title>
<link rel="stylesheet" href="https://fonts.googleapis.com/css2?family=Arimo:wght@400;700&display=swap">
<style>
  :root {
    --backdrop: #dbdbdb;
    --paper: #ffffff;
    --navy: #1f4176;
    --band-grey: #bbbcc0;
    --tagline-grey: #9a9a9e;
  }
  html, body {
    margin: 0;
    padding: 0;
    width: 1200px;
    height: 947px;
    overflow: hidden;
    background: var(--backdrop);
  }
  .canvas {
    position: relative;
    width: 1200px;
    height: 947px;
  }
  .letterhead {
    position: absolute;
    left: 364px;
    top: 179px;
    width: 472px;
    height: 606px;
    background: var(--paper);
  }
  .band {
    position: absolute;
    left: 0;
    width: 472px;
    display: block;
  }
  .band--top { top: 0; height: 14px; }
  .band--bottom { bottom: 0; height: 19px; }
  .band .grey { fill: var(--band-grey); }
  .band .navy { fill: var(--navy); }
  .brand {
    position: absolute;
    top: 17px;
    left: 0;
    width: 100%;
    text-align: center;
    font-family: "Arimo", Arial, sans-serif;
  }
  .brand__name {
    display: block;
    font-size: 23px;
    font-weight: 700;
    letter-spacing: -0.6px;
    line-height: 24px;
    color: var(--navy);
  }
  .brand__tagline {
    display: block;
    font-size: 7.6px;
    font-weight: 400;
    letter-spacing: 0.1px;
    line-height: 9px;
    color: var(--tagline-grey);
  }
</style>
</head>
<body>
<div class="canvas">
  <div class="letterhead">
    <svg class="band band--top" viewBox="0 0 472 14" preserveAspectRatio="none" aria-hidden="true">
      <polygon class="grey" points="0,0 240.6,0 234.6,14 0,14"/>
      <polygon class="navy" points="244.8,0 472,0 472,13.2 239.2,13.2"/>
    </svg>
    <div class="brand">
      <span class="brand__name">Brixley</span>
      <span class="brand__tagline">TRAVEL CORPORATION</span>
    </div>
    <svg class="band band--bottom" viewBox="0 0 472 19" preserveAspectRatio="none" aria-hidden="true">
      <polygon class="grey" points="0,0.6 236,0.6 225.6,19 0,19"/>
      <polygon class="navy" points="240.6,0 472,0 472,19 228.6,19"/>
    </svg>
  </div>
</div>
</body>
</html>
```